Pebble Grocer

Hope all is well!

Wanted to make business cards for my father. His name is Samir Haddad and owns convenience stores. I have attached logo :)

He does not want any title just simple name and phone. An email would be nice as well.

Samir Haddad
Cell: 413-555-0148
Store: 413-555-0192

Pebblegrocer518@mailnest.example

The design and style is totally up to you :) The colors we were looking for were the same as logo :)

```html
<!DOCTYPE html>
<html lang="en">
<head>
<meta charset="UTF-8">
<title>Pebble Grocer — Business Card</title>
<link href="https://fonts.googleapis.com/css2?family=Montserrat:wght@400;700&display=swap" rel="stylesheet">
<style>
  :root {
    --navy: #213776;
    --red: #e8353b;
    --white: #ffffff;
    --backdrop: #1c1c1e;
  }
  * { margin: 0; padding: 0; box-sizing: border-box; }
  html, body {
    width: 1200px;
    height: 900px;
    overflow: hidden;
    background: var(--backdrop);
    font-family: "Montserrat", sans-serif;
  }
  .canvas {
    width: 1200px;
    height: 900px;
    display: flex;
    align-items: center;
    justify-content: center;
  }
  .card {
    position: relative;
    width: 1000px;
    height: 572px;
    background: var(--navy);
    border-radius: 34px;
    overflow: hidden;
  }
  .brand {
    position: absolute;
    left: 80px;
    top: 215px;
    display: flex;
    align-items: center;
    gap: 18px;
  }
  .brand-dot {
    width: 44px;
    height: 44px;
    border-radius: 50%;
    background: var(--white);
    flex: none;
  }
  .brand-name {
    color: var(--white);
    font-weight: 700;
    font-size: 46px;
    letter-spacing: 0.5px;
    line-height: 1;
    white-space: nowrap;
  }
  .divider {
    position: absolute;
    left: 520px;
    top: 150px;
    width: 2px;
    height: 240px;
    background: var(--red);
  }
  .contact {
    position: absolute;
    left: 560px;
    top: 168px;
    color: var(--white);
  }
  .contact-name {
    color: var(--red);
    font-weight: 700;
    font-size: 38px;
    margin-bottom: 30px;
    white-space: nowrap;
  }
  .contact-list { list-style: none; }
  .contact-item {
    display: flex;
    align-items: center;
    gap: 12px;
    font-size: 21px;
    line-height: 1;
    margin-bottom: 18px;
    white-space: nowrap;
  }
  .contact-item svg { width: 20px; height: 20px; flex: none; fill: var(--red); }
  .contact-label { font-size: 13px; margin-left: 6px; }
  .edge-band {
    position: absolute;
    left: 0;
    bottom: 0;
    width: 100%;
    height: 24px;
    display: flex;
  }
  .edge-band-red { width: 44%; background: var(--red); }
  .edge-band-white { flex: 1; background: var(--white); }
</style>
</head>
<body>
<main class="canvas">
  <section class="card">
    <div class="brand">
      <span class="brand-dot"></span>
      <span class="brand-name">Pebble Grocer</span>
    </div>

    <div class="divider"></div>

    <div class="contact">
      <p class="contact-name">Samir Haddad</p>
      <ul class="contact-list">
        <li class="contact-item">
          <svg viewBox="0 0 24 24" aria-hidden="true"><path d="M6.6 10.8a15.1 15.1 0 0 0 6.6 6.6l2.2-2.2a1 1 0 0 1 1-.25 11.4 11.4 0 0 0 3.6.57 1 1 0 0 1 1 1V20a1 1 0 0 1-1 1A17 17 0 0 1 3 4a1 1 0 0 1 1-1h3.5a1 1 0 0 1 1 1c0 1.25.2 2.45.57 3.57a1 1 0 0 1-.25 1z"/></svg>
          <span>413-555-0148<span class="contact-label">(Call)</span></span>
        </li>
        <li class="contact-item">
          <svg viewBox="0 0 24 24" aria-hidden="true"><path d="M2 8c0-2 4-4 10-4s10 2 10 4v2h-5V8.5c-1.5-.6-3-.8-5-.8s-3.5.2-5 .8V10H2zM6 12h12l3 8H3z"/></svg>
          <span>413-555-0192<span class="contact-label">(Store)</span></span>
        </li>
        <li class="contact-item">
          <svg viewBox="0 0 24 24" aria-hidden="true"><path d="M3 5h18v14H3zm2 2v.5l7 5 7-5V7l-7 5z"/></svg>
          <span>Pebblegrocer518@mailnest.example</span>
        </li>
      </ul>
    </div>

    <div class="edge-band" role="img" aria-label="Bottom edge band with a row of small stars, red on the left and white on the right">
      <span class="edge-band-red"></span>
      <span class="edge-band-white"></span>
    </div>
  </section>
</main>
</body>
</html>
```